Psychiatric Office Needs a Website- 1st Time Ever!

Been in practice since 2003 with no website, but finally ready to dive in. We are Maplecrest Behavioral Healthcare, a mental health outpatient practice based in Fayetteville, Georgia that sees diverse individuals and families from childhood to advanced age for a variety of conditions. We've grown by word of mouth and referral but would now like to have a digital footprint. Be the pioneer of our website and we will be sure to share. We would like to see designs that are modern, animated, fairly colorful, easy to read, and caters to all ages. Also, we would like the design to take the whole page (not be centered) and can be viewed well on phone/tablet. Please see our outline for more information. Our motto/slogan is: Maplecrest Behavioral Healthcare- A step forward in your wellness journey, so the design should try to reflect that.
Updates

Target Market(s)

Children through elderly

Industry/Entity Type

Medical

Logo Text

Stepping forward in your wellness journey

Number of Pages Required

1 page

Colors

Designer to choose colors to be used in the design.

Requirements
Must have
• Animation or moving pictures.
• Color.
• Concise.
• User friendly
• Diversity in the stock photos

```html
<!DOCTYPE html>
<html lang="en">
<head>
<meta charset="utf-8">
<title>Maplecrest Behavioral Healthcare</title>
<link rel="stylesheet" href="https://fonts.googleapis.com/css2?family=Roboto+Condensed:wght@400;700&family=Open+Sans:wght@400;600&display=swap">
<style>
:root{
  --blue:#2f7bb6;
  --sky:#4fbbe6;
  --green:#7cc242;
  --ink:#222426;
  --nav:#2a2c2e;
  --panel:#333537;
  --mist:#ececec;
  --sage:#e3e7dc;
  --white:#ffffff;
  --grey:#6d6f72;
}
*{margin:0;padding:0;box-sizing:border-box}
html,body{width:1200px;height:3651px;overflow:hidden}
body{position:relative;background:var(--mist);font-family:'Open Sans',sans-serif;color:var(--ink)}
.abs{position:absolute}
.cond{font-family:'Roboto Condensed',sans-serif}
.topbar{left:0;top:0;width:1200px;height:68px;background:var(--white)}
.topinfo{top:22px;font-size:17px;color:var(--blue);display:flex;align-items:center;gap:10px;font-family:'Roboto Condensed',sans-serif}
.portal-sm{left:994px;top:17px;width:118px;height:36px;background:var(--green);color:var(--white);font-size:14px;display:flex;align-items:center;justify-content:center;font-family:'Roboto Condensed',sans-serif}
.hero{left:0;top:68px;width:1200px;height:560px;background:linear-gradient(90deg,#6f7275 0%,#9a9c9e 45%,#cfc9bd 70%,#8e8a84 100%)}
.navbar{left:0;top:68px;width:1200px;height:66px;background:var(--nav)}
.nav{right:88px;top:68px;height:66px;display:flex;align-items:center;gap:42px;color:var(--white);font-family:'Roboto Condensed',sans-serif;font-size:16px}
.logo{left:85px;top:0;width:190px;height:214px;background:var(--green);border-radius:0 0 12px 12px;display:flex;flex-direction:column;align-items:center;justify-content:center;gap:14px;padding:0 14px;text-align:center}
.logo .dot{width:58px;height:58px;border-radius:50%;background:var(--white)}
.logo .name{color:var(--white);font-family:'Roboto Condensed',sans-serif;font-weight:700;font-size:20px;line-height:1.15}
.hero-title{left:86px;top:312px;color:var(--white);font-size:29px;font-weight:700;letter-spacing:.5px}
.hero-tag{left:87px;top:354px;color:#eef3f6;font-size:14px;letter-spacing:2.4px}
.btn{display:flex;align-items:center;justify-content:center;color:var(--white);font-family:'Roboto Condensed',sans-serif}
.hero-btn{left:88px;top:392px;width:228px;height:61px;background:var(--sky);font-size:18px}
.dots{left:86px;top:476px;display:flex;gap:5px}
.dots span{width:14px;height:14px;border-radius:50%;border:2px solid #555;background:#aaa}
.dots span.on{background:var(--blue);border-color:var(--blue)}
.section-title{left:0;width:1200px;text-align:center;font-family:'Roboto Condensed',sans-serif;font-size:34px}
.card{background:var(--white)}
.card .ph{width:100%;height:166px}
.card .label{height:65px;background:var(--panel);color:var(--white);font-size:13px;display:flex;align-items:center;justify-content:center;text-align:center;padding:0 14px;font-family:'Roboto Condensed',sans-serif;line-height:1.3}
.card .label.active{background:var(--green)}
.arrow{width:56px;height:56px;background:var(--white);display:flex;align-items:center;justify-content:center;box-shadow:0 1px 4px rgba(0,0,0,.2)}
.about{left:0;top:1124px;width:1200px;height:543px;background:linear-gradient(180deg,#2a2a2a,#4a4540 55%,#2b2a28)}
.box{background:var(--white);height:176px;padding:50px 36px 0;font-size:13px;line-height:1.55;color:#444}
.tab{top:-24px;left:0;width:128px;height:48px;background:var(--sky);color:var(--white);font-family:'Roboto Condensed',sans-serif;font-size:19px;display:flex;align-items:center;padding-left:24px}
.more{left:499px;top:1533px;width:202px;height:66px;background:var(--green);font-size:20px}
.news{background:var(--white);border:1px solid #ddd;padding:6px}
.news .ph{height:170px;position:relative}
.date{position:absolute;right:0;top:0;background:var(--blue);color:var(--white);display:flex;align-items:center;gap:6px;padding:6px 10px;font-family:'Roboto Condensed',sans-serif}
.date b{font-size:34px;font-weight:700;line-height:1}
.date span{font-size:13px;line-height:1.1}
.news-title{font-family:'Roboto Condensed',sans-serif;font-size:18px}
.news-text{font-size:12px;color:var(--grey);line-height:1.55}
.news-more{font-size:12px;font-weight:600}
.faq{left:0;top:2244px;width:1200px;height:477px;background:var(--sage)}
.q{left:185px;width:828px;background:var(--panel);color:var(--white);font-family:'Roboto Condensed',sans-serif;font-size:17px;padding:0 26px;border-radius:3px}
.q .row{height:78px;display:flex;align-items:center;justify-content:space-between}
.q.open{background:var(--blue)}
.q .ans{font-family:'Open Sans',sans-serif;font-size:13px;margin-top:-14px}
.q .ans u{color:#cde8fb}
.foot{left:0;top:2721px;width:1200px;height:840px;background:linear-gradient(180deg,#0c0d0f,#15181c 60%,#0d0e10)}
.foot-text{left:285px;width:630px;top:2826px;text-align:center;color:#b9bcc0;font-size:15px;line-height:1.75}
.contact-line{left:88px;color:var(--white);font-size:15px;display:flex;align-items:center;gap:22px}
.field{left:681px;width:396px;border-bottom:1px solid rgba(255,255,255,.75);color:var(--white);font-size:15px;padding-bottom:14px}
.copy{left:0;top:3561px;width:1200px;height:90px;background:var(--sky);color:var(--white);font-size:13px;display:flex;align-items:center;justify-content:center}
</style>
</head>
<body>

<header>
  <div class="abs topbar"></div>
  <div class="abs topinfo" style="left:562px">
    <svg width="16" height="16" viewBox="0 0 24 24"><path fill="#2f7bb6" d="M6.6 10.8a15 15 0 0 0 6.6 6.6l2.2-2.2c.3-.3.7-.4 1-.2 1.1.4 2.3.6 3.6.6.6 0 1 .4 1 1V20c0 .6-.4 1-1 1A17 17 0 0 1 3 4c0-.6.4-1 1-1h3.5c.6 0 1 .4 1 1 0 1.3.2 2.5.6 3.6.1.3 0 .7-.2 1z"/></svg>
    Phone: (770) 555-0142
  </div>
  <div class="abs topinfo" style="left:776px">
    <svg width="16" height="16" viewBox="0 0 24 24"><circle cx="12" cy="12" r="9" fill="none" stroke="#2f7bb6" stroke-width="2.5"/><path d="M12 7v5l3 2" stroke="#2f7bb6" stroke-width="2.5" fill="none"/></svg>
    Hours: M-F 9am-5pm
  </div>
  <div class="abs portal-sm">PATIENT PORTAL</div>

  <div class="abs hero" role="img" aria-label="Photo of an open hand holding a glowing brain against a soft grey background"></div>
  <svg class="abs" style="left:0;top:560px" width="1200" height="70" viewBox="0 0 1200 70">
    <path d="M0 0 C300 55 800 60 1200 10 L1200 70 L0 70Z" fill="#ececec"/>
    <path d="M0 0 C300 55 800 60 1200 10 L1200 28 C800 72 300 70 0 14Z" fill="#7cc242"/>
  </svg>
  <div class="abs navbar"></div>
  <nav class="abs nav"><span>HOME</span><span>ABOUT US</span><span>SERVICES</span><span>CONDITIONS WE TREAT</span><span>NEW PATIENTS</span><span>CONTACT US</span></nav>
  <div class="abs logo"><div class="dot"></div><div class="name">Maplecrest Behavioral Healthcare</div></div>

  <div class="abs hero-title cond">MAPLECREST BEHAVIORAL HEALTHCARE</div>
  <div class="abs hero-tag">A STEP FORWARD IN YOUR WELLNESS JOURNEY</div>
  <div class="abs btn hero-btn">PATIENT PORTAL</div>
  <div class="abs dots"><span></span><span></span><span class="on"></span><span></span><span></span></div>
</header>

<section>
  <h2 class="abs section-title" style="top:728px;font-weight:400">OUR SERVICES</h2>
  <div class="abs card" style="left:90px;top:803px;width:243px">
    <div class="ph" role="img" aria-label="Child giving a high five to a clinician" style="background:linear-gradient(135deg,#e9e4dc,#c9d7df)"></div>
    <div class="label">DIAGNOSTIC EVALUATION AND TREATMENT</div>
  </div>
  <div class="abs card" style="left:348px;top:803px;width:243px">
    <div class="ph" role="img" aria-label="Medicine bottles and a glass on a wooden table" style="background:linear-gradient(135deg,#8a6a48,#c2a27a)"></div>
    <div class="label active">PSYCHOPHARMACOLOGY</div>
  </div>
  <div class="abs card" style="left:608px;top:803px;width:244px">
    <div class="ph" role="img" aria-label="Waist being measured with a tape" style="background:linear-gradient(135deg,#e4e4e4,#caa996)"></div>
    <div class="label">BARIATRIC PRE-SURGICAL CONSULTATION (AND OTHER SURGERIES)</div>
  </div>
  <div class="abs card" style="left:869px;top:803px;width:241px">
    <div class="ph" role="img" aria-label="Wheelchair user with raised arms on a beach" style="background:linear-gradient(180deg,#7fbfe6,#5a9ec4 60%,#d9c9a4)"></div>
    <div class="label">DISABILITY AND WORK-RELATED REPORTS (INCLUDE?)</div>
  </div>
  <div class="abs arrow" style="left:58px;top:891px"><svg width="18" height="22" viewBox="0 0 18 22"><path d="M14 2 4 11l10 9" stroke="#222" stroke-width="3" fill="none"/></svg></div>
  <div class="abs arrow" style="left:1080px;top:891px"><svg width="18" height="22" viewBox="0 0 18 22"><path d="M4 2l10 9-10 9" stroke="#222" stroke-width="3" fill="none"/></svg></div>
</section>

<section>
  <div class="abs about" role="img" aria-label="Dark dusk field with a person raising their arms"></div>
  <h2 class="abs section-title" style="top:1215px;color:var(--white);font-weight:400">ABOUT MBHC</h2>
  <div class="abs box" style="left:122px;top:1317px;width:469px">
    <div class="abs tab">VISION</div>
    To be the leading provider of outpatient psychiatric care in Atlanta Metro South, working together to promote (the) mental wellness of our community.
  </div>
  <div class="abs box" style="left:621px;top:1317px;width:457px">
    <div class="abs tab">MISSION</div>
    To provide mental health services to children, adults, and the developmentally disabled population that is culturally sensitive regardless of age, race, gender, orientation, religion, or creed;<br>To work hand in hand with clients to overcome mental health challenges and improve their quality of life.
  </div>
  <div class="abs btn more">READ MORE &gt;</div>
</section>

<section>
  <h2 class="abs section-title" style="top:1772px;font-weight:400">LATEST NEWS</h2>
  <div class="abs arrow" style="left:1054px;top:1802px;width:24px;height:24px;box-shadow:none;border:1px solid #bbb;background:none"><svg width="8" height="10" viewBox="0 0 8 10"><path d="M6 1 2 5l4 4" stroke="#888" stroke-width="1.5" fill="none"/></svg></div>
  <div class="abs arrow" style="left:1086px;top:1802px;width:24px;height:24px;box-shadow:none;border:1px solid #bbb;background:none"><svg width="8" height="10" viewBox="0 0 8 10"><path d="M2 1l4 4-4 4" stroke="#888" stroke-width="1.5" fill="none"/></svg></div>

  <article class="abs news" style="left:88px;top:1862px;width:328px">
    <div class="ph" role="img" aria-label="Person pinching their waist" style="background:linear-gradient(135deg,#d9d9d9,#b08a74)"><div class="date"><b>17</b><span>August<br>2017</span></div></div>
  </article>
  <article class="abs news" style="left:436px;top:1862px;width:328px">
    <div class="ph" role="img" aria-label="Group of smiling young people" style="background:linear-gradient(135deg,#8fb3cf,#6a8f5a)"><div class="date"><b>16</b><span>August<br>2017</span></div></div>
  </article>
  <article class="abs news" style="left:784px;top:1862px;width:328px">
    <div class="ph" role="img" aria-label="Patient talking with a counselor" style="background:linear-gradient(135deg,#f1ece4,#9a5a4e)"><div class="date"><b>15</b><span>August<br>2017</span></div></div>
  </article>
  <div class="abs" style="left:88px;top:2050px;width:328px"><div class="news-title">The standard Lorem Ipsum passage</div><p class="news-text" style="margin-top:8px">Sed ut perspiciatis unde omnis iste natus error sit voluptatem accusantium doloremque laudantium, totam rem aperiam, eaque ipsa quae ab illo inventore...</p><div class="news-more" style="margin-top:6px">Read More &gt;</div></div>
  <div class="abs" style="left:436px;top:2050px;width:328px"><div class="news-title">The standard Lorem Ipsum passage</div><p class="news-text" style="margin-top:8px">Sed ut perspiciatis unde omnis iste natus error sit voluptatem accusantium doloremque laudantium, totam rem aperiam, eaque ipsa quae ab illo inventore...</p><div class="news-more" style="margin-top:6px">Read More &gt;</div></div>
  <div class="abs" style="left:784px;top:2050px;width:328px"><div class="news-title">The standard Lorem Ipsum passage</div><p class="news-text" style="margin-top:8px">Sed ut perspiciatis unde omnis iste natus error sit voluptatem accusantium doloremque laudantium, totam rem aperiam, eaque ipsa quae ab illo inventore...</p><div class="news-more" style="margin-top:6px">Read More &gt;</div></div>
</section>

<section>
  <div class="abs faq"></div>
  <h2 class="abs section-title" style="top:2302px;font-weight:700;font-size:34px">FAQ</h2>
  <div class="abs q open" style="top:2376px;height:104px">
    <div class="row"><span>What do I need to bring with me to my first visit?</span><svg width="16" height="16"><rect x="1" y="1" width="14" height="14" fill="none" stroke="#fff" stroke-width="1.5"/><path d="M4 8h8" stroke="#fff" stroke-width="1.5"/></svg></div>
    <div class="ans">Insurance card, patient forms found on our <u>Form's page.</u></div>
  </div>
  <div class="abs q" style="top:2485px;height:81px"><div class="row"><span>How long do I have to wait to be seen?</span><svg width="16" height="16"><rect x="1" y="1" width="14" height="14" fill="none" stroke="#fff" stroke-width="1.5"/><path d="M4 8h8M8 4v8" stroke="#fff" stroke-width="1.5"/></svg></div></div>
  <div class="abs q" style="top:2573px;height:80px"><div class="row"><span>What typs of insurance do you accept?</span><svg width="16" height="16"><rect x="1" y="1" width="14" height="14" fill="none" stroke="#fff" stroke-width="1.5"/><path d="M4 8h8M8 4v8" stroke="#fff" stroke-width="1.5"/></svg></div></div>
</section>

<footer>
  <div class="abs foot" role="img" aria-label="Dark world map backdrop with faint lights"></div>
  <h2 class="abs section-title" style="top:2770px;color:var(--white);font-weight:400">GET IN TOUCH</h2>
  <p class="abs foot-text">Lorem Ipsum is simply dummy text of the printing and typesetting industry. Lorem Ipsum has been the industry's standard dummy text ever since the 1500s.</p>

  <div class="abs cond" style="left:85px;top:2998px;color:var(--white);font-size:20px">Maplecrest Behavioral Healthcare</div>
  <div class="abs contact-line" style="top:3052px"><svg width="14" height="18" viewBox="0 0 14 18"><path d="M7 0a7 7 0 0 0-7 7c0 5 7 11 7 11s7-6 7-11a7 7 0 0 0-7-7zm0 9.5A2.5 2.5 0 1 1 7 4.5a2.5 2.5 0 0 1 0 5z" fill="#fff"/></svg>48 Orchard Lane, Fayetteville, Georgia, 30214.</div>
  <div class="abs contact-line" style="top:3093px"><svg width="14" height="14" viewBox="0 0 24 24"><path fill="#fff" d="M6.6 10.8a15 15 0 0 0 6.6 6.6l2.2-2.2c.3-.3.7-.4 1-.2 1.1.4 2.3.6 3.6.6.6 0 1 .4 1 1V20c0 .6-.4 1-1 1A17 17 0 0 1 3 4c0-.6.4-1 1-1h3.5c.6 0 1 .4 1 1 0 1.3.2 2.5.6 3.6.1.3 0 .7-.2 1z"/></svg>(770) 555-0142</div>
  <div class="abs contact-line" style="top:3137px"><svg width="16" height="12" viewBox="0 0 16 12"><rect width="16" height="12" fill="#fff"/><path d="M0 0l8 7 8-7" stroke="#15181c" stroke-width="1.5" fill="none"/></svg>info@maplecrestbh.com</div>

  <div class="abs cond" style="left:85px;top:3222px;color:var(--white);font-size:20px">SUBSCRIBE</div>
  <div class="abs" style="left:88px;top:3269px;width:306px;height:51px;border:1px solid #cfd2d6;color:#9a9da1;font-size:14px;padding:14px 18px">Email Address</div>
  <div class="abs btn" style="left:88px;top:3335px;width:126px;height:39px;background:var(--green);font-size:15px">SUBMIT</div>
  <div class="abs cond" style="left:85px;top:3434px;color:var(--white);font-size:20px">FOLLOW US</div>
  <div class="abs" style="left:214px;top:3428px;width:40px;height:40px;border-radius:50%;background:var(--blue)"></div>

  <div class="abs" style="left:647px;top:2957px;width:465px;height:514px;background:var(--blue)"></div>
  <div class="abs cond" style="left:647px;top:2998px;width:465px;text-align:center;color:var(--white);font-size:24px">CONTACT US</div>
  <div class="abs field" style="top:3068px">Name</div>
  <div class="abs field" style="top:3148px">Phone</div>
  <div class="abs field" style="top:3228px">Email</div>
  <div class="abs field" style="top:3308px">Message...</div>
  <div class="abs btn" style="left:913px;top:3395px;width:158px;height:47px;background:var(--green);font-size:18px">SUBMIT</div>
</footer>

<div class="abs copy">Copyright (c) 2017. Maplecrest Behavioral Healthcare. All rights reserved.</div>
</body>
</html>
```